TECH PROJECT NEEDS NEW SKINS FOR RE-BRANDING

We are a technology project that has a product (crypto wallet) nearing release, have basic designs made so far however we need NEW SKINS/ branding/ design options for this wallet to change the look and feel -- it will be called and re-branded as "KESTRIL" a futuristic/ space/ edgy product so need it to look like so.

YOU ARE ALLOWED TO CHANGE + EXPERIMENT WITH THE LAYOUT/ schema and UI as you see fit -- (we are open to new and creative ideas)

(see WALLET.PNG and PROTFOLIO.PNG ATTACHED --- these are the pages we need new skins for )

(see KESTRIL logo attached --- PLEASE USE THIS LOGO/ VERSIONS OF THIS LOGO IN YOUR DESIGNS/SKIN SUBMISSIONS -- WE PROVIDED THE ai file so feel free to alter the logo a bit to experiment if you want -- we are open and flexible to new creative ideas)

(FOR A MOOD BOARD FOR GUIDANCE on feel/colors/mood-- SEE "SAMPLE INTERFACE 1 & 2" ATTACHED)

Target Market(s)

TECHNOLOGY/SPACE/ FUTURE

Number of Pages Required

2 page

Colors

Designer to choose colors to be used in the design.

Requirements
Must have
• MUST USE OUR KESTRIL LOGO OR A SIMILAR ALTERATION OF IT

```html
<!DOCTYPE html>
<html lang="en">
<head>
<meta charset="utf-8">
<title>KESTRIL Wallet – Stellanet-SLN</title>
<link href="https://fonts.googleapis.com/css2?family=Open+Sans:wght@400;600&display=swap" rel="stylesheet">
<style>
:root{
  --bg:#0a1820;
  --nav:#0b1c25;
  --panel:#0d1c25;
  --line:#13303c;
  --row:#0b1b23;
  --row-border:#15313c;
  --teal:#22bfe0;
  --teal-dark:#1d8597;
  --text:#ffffff;
  --muted:#a9b6bd;
  --blue:#4f7cff;
  --green:#2fd05a;
  --amber:#e8892a;
  --selected:#0f1e3a;
  --selected-border:#1f2f78;
  --field:#08141b;
  --footer:#000000;
}
*{box-sizing:border-box;margin:0;padding:0}
html,body{width:1200px;height:910px;overflow:hidden;background:var(--bg);font-family:"Open Sans",sans-serif;color:var(--text)}
.app{position:relative;width:1200px;height:910px}

.nav{position:absolute;left:0;top:0;width:136px;height:862px;background:var(--nav);border-right:1px solid var(--line)}
.brand{height:120px;display:flex;flex-direction:column;align-items:center;justify-content:center;gap:8px;border-bottom:1px solid var(--line)}
.brand-mark{width:30px;height:30px;border-radius:50%;background:var(--teal)}
.brand-name{font-size:17px;letter-spacing:2px;color:var(--teal);font-weight:600}
.nav-item{height:85px;display:flex;flex-direction:column;align-items:center;justify-content:center;gap:8px;font-size:13.5px;border-bottom:1px solid var(--line)}
.nav-item svg{width:20px;height:20px;fill:#fff}
.nav-item.active{background:var(--teal-dark)}
.nav-item.settings{position:absolute;bottom:0;left:0;width:135px;border-top:1px solid var(--line);border-bottom:none}

.wallets{position:absolute;left:136px;top:0;width:220px;height:862px;background:var(--panel);border-right:1px solid var(--line)}
.wallets h1{position:absolute;left:26px;top:33px;font-size:22px;font-weight:400}
.wallets .sub{position:absolute;left:26px;top:67px;font-size:13.5px}
.search{position:absolute;display:flex;align-items:center;justify-content:space-between;background:var(--field);color:var(--muted);font-size:12px;padding:0 18px}
.search svg{width:12px;height:12px;fill:#fff}
.wallets .search{left:26px;top:120px;width:180px;height:34px}
.coin{position:absolute;left:0;width:222px;height:67px;display:flex;align-items:center;padding-left:24px;gap:14px}
.coin.selected{background:var(--selected);border:1px solid var(--selected-border);left:1px}
.hex{width:42px;height:46px;flex:none}
.coin-name{font-size:12.5px;font-weight:600}
.coin-bal{font-size:10px;color:var(--muted);margin-top:6px}

.main{position:absolute;left:356px;top:0;width:844px;height:862px}
.title{position:absolute;left:48px;top:22px;display:flex;align-items:center;gap:12px}
.title .hex{width:54px;height:60px}
.title h2{font-size:24px;font-weight:400}
.rate{position:absolute;left:585px;top:34px;width:180px;height:38px;border:2px solid var(--selected-border);display:flex;align-items:center;justify-content:center;font-size:14px}
.label{color:var(--teal);font-size:14px}
.balance-label{position:absolute;left:48px;top:112px;font-weight:600}
.balance{position:absolute;left:48px;top:132px;font-size:27px}
.balance-usd{position:absolute;left:48px;top:173px;font-size:14px}
.btn{position:absolute;top:132px;width:166px;height:40px;border:1px solid #c9d3d8;display:flex;align-items:center;justify-content:center;gap:7px;font-size:14px}
.btn svg{width:13px;height:13px}
.btn.send{left:415px}
.btn.receive{left:599px}
.addr-label{position:absolute;left:49px;top:227px;font-size:13px;color:#2ba5c4}
.addr{position:absolute;left:49px;top:252px;font-size:13.5px}
.copy{position:absolute;left:287px;top:252px;font-size:13.5px;color:var(--teal);display:flex;gap:5px;align-items:center}
.copy svg{width:13px;height:13px;fill:none;stroke:var(--teal);stroke-width:1.5}
.main .search{left:415px;top:233px;width:350px;height:36px}

.table{position:absolute;left:36px;top:315px;width:775px}
.thead{display:flex;height:40px;background:#0b1a22;font-size:11px;color:#c8d1d6;align-items:center}
.tr{display:flex;height:45px;margin-top:5px;background:var(--row);border:1px solid var(--row-border);font-size:10.5px;align-items:center}
.tbody{margin-top:6px}
.c{height:100%;display:flex;align-items:center;border-right:1px solid var(--row-border)}
.c:last-child{border-right:none}
.thead .c{border:none}
.c1{width:120px;padding-left:18px;gap:5px}
.c2{width:96px;justify-content:center}
.c3{width:186px;justify-content:center}
.c4{width:99px;justify-content:center}
.c5{width:83px;justify-content:center}
.c6{width:114px;justify-content:center}
.c7{width:77px;justify-content:center}
.thead .sorted{position:relative}
.thead .sorted::after{content:"";position:absolute;left:23px;right:11px;bottom:0;height:2px;background:var(--teal)}
.dot{width:9px;height:9px;border-radius:50%;flex:none}
.dot.out{background:var(--blue)}
.dot.in{background:var(--green)}
.pending{color:var(--amber)}
.success{color:var(--green)}
.details{color:var(--teal)}

.footer{position:absolute;left:0;top:862px;width:1200px;height:48px;background:var(--footer);display:flex;align-items:center;justify-content:center;font-size:12.5px}
</style>
</head>
<body>
<div class="app">
  <nav class="nav">
    <div class="brand"><span class="brand-mark"></span><span class="brand-name">KESTRIL</span></div>
    <div class="nav-item"><svg viewBox="0 0 20 20"><rect x="0" y="2" width="5" height="4"/><rect x="7" y="2" width="6" height="4"/><rect x="15" y="2" width="5" height="4"/><rect x="0" y="8" width="5" height="4"/><rect x="7" y="8" width="6" height="4"/><rect x="15" y="8" width="5" height="4"/><rect x="0" y="14" width="5" height="4"/><rect x="7" y="14" width="6" height="4"/><rect x="15" y="14" width="5" height="4"/></svg>Dashboard</div>
    <div class="nav-item"><svg viewBox="0 0 20 20"><path d="M3 0h10l5 5v15H3z M5 2v16h11V6h-4V2z M6 16l3-5 2 3 2-2 2 4z"/><circle cx="8" cy="8" r="1.6"/></svg>Portfolio</div>
    <div class="nav-item active"><svg viewBox="0 0 20 20"><path d="M1 3h18v14H1z M3 5v2h14V5z M3 10v5h14v-5z M4 12h5v1.5H4z"/></svg>Wallets</div>
    <div class="nav-item"><svg viewBox="0 0 20 20"><path d="M11 0L4 11h5l-2 9 8-12h-5z"/></svg>Lightning</div>
    <div class="nav-item"><svg viewBox="0 0 20 20"><path d="M5 17a4 4 0 010-8 6 6 0 0111-1 4.5 4.5 0 010 9z"/></svg>SLN Cloud</div>
    <div class="nav-item settings"><svg viewBox="0 0 20 20"><path d="M8.5 0h3l.5 2.6 2 .9 2.2-1.5 2.1 2.1-1.5 2.2.9 2 2.6.5v3l-2.6.5-.9 2 1.5 2.2-2.1 2.1-2.2-1.5-2 .9-.5 2.6h-3L8 17.4l-2-.9-2.2 1.5-2.1-2.1 1.5-2.2-.9-2L0 11.5v-3L2.6 8l.9-2L2 3.8 4.1 1.7 6.3 3.2 8 2.6z M10 6.5a3.5 3.5 0 100 7 3.5 3.5 0 000-7z"/></svg>Settings</div>
  </nav>

  <aside class="wallets">
    <h1>Wallets</h1>
    <div class="sub">6 Active Wallets</div>
    <div class="search">Search..<svg viewBox="0 0 12 12"><path d="M5 0a5 5 0 013.9 8.1l3 3-1 1-3-3A5 5 0 115 0zm0 2a3 3 0 100 6 3 3 0 000-6z"/></svg></div>

    <div class="coin" style="top:180px"><svg class="hex" viewBox="0 0 42 46"><polygon points="21,1 40,12 40,34 21,45 2,34 2,12" fill="#141a1a" stroke="#c4812a" stroke-width="2"/><circle cx="21" cy="23" r="5" fill="#fff"/></svg><div><div class="coin-name">Nebulon-NBL</div><div class="coin-bal">10.21000192 NBL</div></div></div>
    <div class="coin" style="top:249px"><svg class="hex" viewBox="0 0 42 46"><polygon points="21,1 40,12 40,34 21,45 2,34 2,12" fill="#0f1b2e" stroke="#1e63c4" stroke-width="2"/><circle cx="21" cy="23" r="5" fill="#fff"/></svg><div><div class="coin-name">Quasar-QSR</div><div class="coin-bal">30.51 QSR</div></div></div>
    <div class="coin" style="top:318px"><svg class="hex" viewBox="0 0 42 46"><polygon points="21,1 40,12 40,34 21,45 2,34 2,12" fill="#170f2a" stroke="#6a27c8" stroke-width="2"/><circle cx="21" cy="23" r="5" fill="#fff"/></svg><div><div class="coin-name">Aetherion-AET</div><div class="coin-bal">1,100.00 AET</div></div></div>
    <div class="coin" style="top:387px"><svg class="hex" viewBox="0 0 42 46"><polygon points="21,1 40,12 40,34 21,45 2,34 2,12" fill="#141a1e" stroke="#2a3238" stroke-width="2"/><circle cx="21" cy="23" r="5" fill="#fff"/></svg><div><div class="coin-name">Lumenis-LMN</div><div class="coin-bal">961.005 LMN</div></div></div>
    <div class="coin" style="top:456px"><svg class="hex" viewBox="0 0 42 46"><polygon points="21,1 40,12 40,34 21,45 2,34 2,12" fill="#0f1d28" stroke="#2f5f80" stroke-width="2"/><circle cx="21" cy="23" r="5" fill="#fff"/></svg><div><div class="coin-name">Tidalis-TDL</div><div class="coin-bal">210.0176 TDL</div></div></div>
    <div class="coin selected" style="top:528px"><svg class="hex" viewBox="0 0 42 46"><polygon points="21,1 40,12 40,34 21,45 2,34 2,12" fill="#0d1430" stroke="#1c2a6a" stroke-width="2"/><circle cx="21" cy="23" r="5" fill="#fff"/></svg><div><div class="coin-name">Stellanet-SLN</div><div class="coin-bal">369,800.00 SLN</div></div></div>
  </aside>

  <main class="main">
    <div class="title"><svg class="hex" viewBox="0 0 54 60"><polygon points="27,1 52,15 52,45 27,59 2,45 2,15" fill="#0d1430" stroke="#1c2a6a" stroke-width="2"/><circle cx="27" cy="30" r="7" fill="#fff"/></svg><h2>Stellanet-SLN</h2></div>
    <div class="rate">1SLN = 0.08 USD</div>

    <div class="label balance-label">Balance</div>
    <div class="balance">369,800.00 SLN</div>
    <div class="balance-usd">=29,584.00 USD</div>

    <div class="btn send"><svg viewBox="0 0 14 14"><circle cx="7" cy="7" r="7" fill="#22bfe0"/><path d="M7 3L3.5 7H6v4h2V7h2.5z" fill="#0a1820"/></svg>SEND MONEY</div>
    <div class="btn receive"><svg viewBox="0 0 14 14"><circle cx="7" cy="7" r="7" fill="#22bfe0"/><path d="M7 11l3.5-4H8V3H6v4H3.5z" fill="#0a1820"/></svg>RECEIVE MONEY</div>

    <div class="addr-label">WALLET ADDRESS</div>
    <div class="addr">VbpykoRwGPr3nGPbjYNT7eKans</div>
    <div class="copy"><svg viewBox="0 0 14 14"><rect x="1" y="4" width="8" height="9"/><path d="M5 4V1h8v9h-4"/></svg>Copy</div>
    <div class="search">Search Transactions..<svg viewBox="0 0 12 12"><path d="M5 0a5 5 0 013.9 8.1l3 3-1 1-3-3A5 5 0 115 0zm0 2a3 3 0 100 6 3 3 0 000-6z"/></svg></div>

    <div class="table">
      <div class="thead">
        <div class="c c1">ACTIVITY</div><div class="c c2 sorted" style="font-weight:600;color:#fff">DATE</div><div class="c c3">TRANSACTIONS ID</div><div class="c c4">AMOUNT</div><div class="c c5">STATUS</div><div class="c c6">BALANCE CHANGE</div><div class="c c7">DETAILS</div>
      </div>
      <div class="tbody">
        <div class="tr"><div class="c c1"><span class="dot out"></span>Sending Money</div><div class="c c2">15 Feb 2019</div><div class="c c3">25hdyhg2154dfhGFndhfnkjk...</div><div class="c c4">219.82 SLN</div><div class="c c5 pending">PENDING</div><div class="c c6">369,800.00 SLN</div><div class="c c7 details">DETAILS</div></div>
        <div class="tr"><div class="c c1"><span class="dot in"></span>Money Received</div><div class="c c2">14 Feb 2019</div><div class="c c3">25hdyhg2154dfhGFndhfnkjk...</div><div class="c c4">219.82 SLN</div><div class="c c5 success">SUCCESS</div><div class="c c6">369,800.00 SLN</div><div class="c c7 details">DETAILS</div></div>
        <div class="tr"><div class="c c1"><span class="dot out"></span>Sending Money</div><div class="c c2">14 Feb 2019</div><div class="c c3">25hdyhg2154dfhGFndhfnkjk...</div><div class="c c4">2700.00 SLN</div><div class="c c5 success">SUCCESS</div><div class="c c6">369,800.00 SLN</div><div class="c c7 details">DETAILS</div></div>
        <div class="tr"><div class="c c1"><span class="dot in"></span>Money Received</div><div class="c c2">15 Feb 2019</div><div class="c c3">25hdyhg2154dfhGFndhfnkjk...</div><div class="c c4">219.82 SLN</div><div class="c c5 success">SUCCESS</div><div class="c c6">369,800.00 SLN</div><div class="c c7 details">DETAILS</div></div>
        <div class="tr"><div class="c c1"><span class="dot out"></span>Sending Money</div><div class="c c2">05 Jan 2019</div><div class="c c3">25hdyhg2154dfhGFndhfnkjk...</div><div class="c c4">219.82 SLN</div><div class="c c5 success">SUCCESS</div><div class="c c6">369,800.00 SLN</div><div class="c c7 details">DETAILS</div></div>
        <div class="tr"><div class="c c1"><span class="dot in"></span>Money Received</div><div class="c c2">20 Dec 2018</div><div class="c c3">25hdyhg2154dfhGFndhfnkjk...</div><div class="c c4">219.82 SLN</div><div class="c c5 success">SUCCESS</div><div class="c c6">369,800.00 SLN</div><div class="c c7 details">DETAILS</div></div>
        <div class="tr"><div class="c c1"><span class="dot out"></span>Sending Money</div><div class="c c2">15 Feb 2019</div><div class="c c3">25hdyhg2154dfhGFndhfnkjk...</div><div class="c c4">219.82 SLN</div><div class="c c5 success">SUCCESS</div><div class="c c6">369,800.00 SLN</div><div class="c c7 details">DETAILS</div></div>
        <div class="tr"><div class="c c1"><span class="dot in"></span>Money Received</div><div class="c c2">15 Nov 2018</div><div class="c c3">25hdyhg2154dfhGFndhfnkjk...</div><div class="c c4">219.82 SLN</div><div class="c c5 success">SUCCESS</div><div class="c c6">369,800.00 SLN</div><div class="c c7 details">DETAILS</div></div>
      </div>
    </div>
  </main>

  <footer class="footer">2019 © Companyname All rights reserved. &nbsp;| &nbsp;Privacy Policy</footer>
</div>
</body>
</html>
```